AUDITING SERVICES FOR IMPORT/EXPORT/LOGISTICS

* PROCUREMENT OF PARTS / SERVICES
* BOAT POSITIONING

Industry/Entity Type

Auditing

Contact Information for Business Card

KTF CONSULTANTS
(WILLOW HARBOUR CRAFT PTY LTD) 17 THE ESPLANADE CORELLA SHORES
DAVID FENWICK 0418274603 LOUISE-JANE FENWICK 0418274681 (ON OPPOSITE SIDE)

```html
<!DOCTYPE html>
<html lang="en">
<head>
<meta charset="utf-8">
<title>KTF Consultants – Business Card</title>
<link rel="stylesheet" href="https://fonts.googleapis.com/css2?family=Tinos&family=PT+Sans&display=swap">
<style>
  :root {
    --sky-top: #25ace4;
    --sky-bottom: #1590cf;
    --band-top: #383838;
    --band-mid: #0a0a0a;
    --band-bottom: #000000;
    --sea-top: #0a72ad;
    --sea-bottom: #003e6f;
    --ink: #ffffff;
  }
  html, body {
    margin: 0;
    padding: 0;
    overflow: hidden;
    background: #ffffff;
  }
  .card {
    position: relative;
    width: 1200px;
    height: 741px;
    overflow: hidden;
    font-family: "PT Sans", "Tahoma", sans-serif;
    color: var(--ink);
  }
  .card__sky {
    position: absolute;
    left: 0; top: 0;
    width: 100%; height: 232px;
    background: linear-gradient(to bottom, var(--sky-top), var(--sky-bottom));
  }
  .card__band {
    position: absolute;
    left: 0; top: 232px;
    width: 100%; height: 186px;
    background: linear-gradient(to bottom, var(--band-top) 0%, var(--band-mid) 28%, var(--band-bottom) 100%);
  }
  .card__sea {
    position: absolute;
    left: 0; top: 418px;
    width: 100%; height: 323px;
    background: linear-gradient(to bottom, var(--sea-top), var(--sea-bottom));
  }
  .company-name {
    position: absolute;
    left: 0; top: 304px;
    width: 1188px;
    margin: 0;
    text-align: center;
    font-family: "Tinos", "Times New Roman", serif;
    font-weight: 400;
    font-size: 49px;
    line-height: 1;
    letter-spacing: 0.5px;
  }
  .tagline {
    position: absolute;
    left: 0; top: 425px;
    width: 1200px;
    margin: 0;
    text-align: center;
    font-size: 37px;
    line-height: 1.1;
  }
  .contact {
    position: absolute;
    top: 496px;
    margin: 0;
    font-style: normal;
    font-size: 29px;
    line-height: 40px;
  }
  .contact--left { left: 55px; text-align: left; }
  .contact--right { right: 56px; text-align: right; }
  .contact__line { display: block; white-space: nowrap; }
  .address {
    position: absolute;
    left: 0; top: 646px;
    width: 1200px;
    margin: 0;
    text-align: center;
    font-style: normal;
    font-size: 29px;
    line-height: 40px;
  }
</style>
</head>
<body>
  <div class="card">
    <div class="card__sky"></div>
    <div class="card__band"></div>
    <div class="card__sea"></div>

    <h1 class="company-name">KTF CONSULTANTS</h1>
    <p class="tagline">Auditing Services for Import/Export/Logistics</p>

    <address class="contact contact--left">
      <span class="contact__line">David Fenwick</span>
      <span class="contact__line">Tel : 61 418 274 603</span>
      <span class="contact__line">Email : david@ktf.net.au</span>
    </address>

    <address class="contact contact--right">
      <span class="contact__line">Louise-Jane Fenwick</span>
      <span class="contact__line">Tel : 61 418 274 681</span>
      <span class="contact__line">Email : louisejane@ktf.net.au</span>
    </address>

    <address class="address">17 The Esplanade Corella Shores Qld 4519</address>
  </div>
</body>
</html>
```